Pebble Lane real estate investment company needs a poster design

We would like a poster design size 18 x 24.
Poster wording -
I WANT TO BUY YOUR ( finish with logo) logo uploaded
website- www.pebblelane-homes.example
phone # 555-217-8843 ( color red for the phone number)
we would like to see the poster on 2 different backgrounds
Yellow background
White background
horizontal

```html
<!DOCTYPE html>
<html lang="en">
<head>
<meta charset="utf-8">
<title>Pebble Lane Poster</title>
<link rel="stylesheet" href="https://fonts.googleapis.com/css2?family=Bebas+Neue&display=swap">
<style>
  :root {
    --page: #f4f4f4;
    --poster-yellow: #e9e32c;
    --poster-yellow-deep: #d9d21f;
    --ink: #111111;
    --alert-red: #e8313b;
    --phone-yellow: #efe52a;
  }
  html, body {
    margin: 0;
    padding: 0;
    width: 1200px;
    height: 1000px;
    overflow: hidden;
    background: var(--page);
  }
  .poster {
    position: absolute;
    left: 50px;
    top: 50px;
    width: 1092px;
    height: 818px;
    font-family: "Bebas Neue", "Arial Narrow", sans-serif;
    color: var(--ink);
  }
  .poster-surface {
    position: absolute;
    inset: 0;
    background: radial-gradient(ellipse at 60% 40%, var(--poster-yellow) 0%, var(--poster-yellow-deep) 100%);
  }
  .frame {
    position: absolute;
    left: 0;
    top: 0;
  }
  .headline {
    position: absolute;
    left: 0;
    width: 1070px;
    margin: 0;
    text-align: center;
    font-weight: 400;
    font-size: 122px;
    line-height: 1;
    letter-spacing: 1px;
  }
  .headline-one { top: 92px; }
  .headline-two { top: 240px; }
  .brand-name {
    position: absolute;
    left: 0;
    width: 1080px;
    top: 386px;
    text-align: center;
    font-size: 124px;
    line-height: 1;
    letter-spacing: 6px;
  }
  .call-now {
    position: absolute;
    left: 0;
    width: 1070px;
    top: 568px;
    text-align: center;
    font-size: 72px;
    line-height: 1;
  }
  .phone-box {
    position: absolute;
    left: 363px;
    top: 637px;
    width: 372px;
    height: 78px;
    background: var(--alert-red);
    color: var(--phone-yellow);
    font-size: 66px;
    line-height: 84px;
    text-align: center;
    letter-spacing: 1px;
  }
  .website {
    position: absolute;
    left: 0;
    width: 1092px;
    top: 738px;
    text-align: center;
    font-size: 28px;
    line-height: 1;
    letter-spacing: 1px;
  }
</style>
</head>
<body>
  <div class="poster">
    <div class="poster-surface" role="img" aria-label="Cracked yellow painted wall texture"></div>
    <svg class="frame" width="1092" height="818" viewBox="0 0 1092 818" aria-hidden="true">
      <g fill="none" stroke="#111111" stroke-width="7">
        <polyline points="360,750 61,750 61,61 1033,61 1033,750 732,750"/>
      </g>
    </svg>
    <h1 class="headline headline-one">I want</h1>
    <h2 class="headline headline-two">to buy your</h2>
    <div class="brand-name">Pebble Lane</div>
    <div class="call-now">Call now!</div>
    <div class="phone-box">555-217-8843</div>
    <div class="website">www.pebblelane-homes.example</div>
  </div>
</body>
</html>
```